Slider needed for Database Documentation Topic

We need a slider to promote a content area of a web site. I'm listing this as a poster because the posters I have seen on Quillbarn portfolios most closely resemble the combination or art and text I am looking for.
The content area we are promoting with this graphic will clarify the design and use of a complicated database. The title of the content area is "The Marbled QZ Database" and the banner should use that title.
To 'illuminate' something means to cast light on it, and this content area will help shed light on a complicated thing – the content will use diagrams, text, and examples to clarify the database. Another meaning is that an illuminated manuscript is a manuscript brought to life with pictures, and in a way that is also what this content area will do.
One idea for the slider might be a light bulb, lamp, candle or flashlight lighting up the words "QZ Database". Another idea would be the type of illustration you see if you search for "Illuminated manuscript"
But I'm not committed to any particular idea - in the past I have been pleased to see ideas that are different than my own but accomplish the same thing, so please feel free to use your judgement or ask any questions.
In addition to the title (The Marbled QZ Database) the graphic should allow room for three smaller lines of text – the three bullet items below:
- Guide to understanding the QZ database
- Data sources, uses and relationships explained with illustrations
- New content! Customers
The last bullet item will change as the content is added.
Some particulars ...
SIZE - 600 high x 1200 wide pixels
PHOTOS vs ILLUSTRATION - I am open to either one.

```html
<!DOCTYPE html>
<html lang="en">
<head>
<meta charset="utf-8">
<title>The Marbled QZ Database — Slider</title>
<link rel="stylesheet" href="https://fonts.googleapis.com/css2?family=Anton&family=Michroma&display=swap">
<style>
  :root {
    --canvas-bg: #e6e6e6;
    --deep: #021114;
    --teal-dark: #06373d;
    --teal: #1f7f88;
    --teal-light: #7fd3dc;
    --beam-core: #f2fdff;
    --title-light: #9fe2ea;
    --title-mid: #3aa3ad;
    --title-shadow: #021a1e;
    --bullet-text: #e9f7f8;
  }

  * { margin: 0; padding: 0; box-sizing: border-box; }

  html, body {
    width: 1200px;
    height: 848px;
    overflow: hidden;
    background: var(--canvas-bg);
  }

  .canvas {
    position: relative;
    width: 1200px;
    height: 848px;
    display: flex;
    align-items: center;
    justify-content: center;
  }

  .slider {
    position: relative;
    width: 1200px;
    height: 600px;
    overflow: hidden;
    background: var(--deep);
  }

  .slider__photo {
    position: absolute;
    inset: 0;
    background:
      radial-gradient(ellipse 38% 20% at 86% 45%, var(--beam-core) 0%, rgba(220, 250, 255, 0.85) 35%, rgba(120, 210, 220, 0) 100%),
      radial-gradient(ellipse 75% 42% at 70% 45%, rgba(150, 225, 232, 0.85) 0%, rgba(40, 140, 150, 0.55) 45%, rgba(6, 55, 61, 0) 100%),
      radial-gradient(ellipse 95% 70% at 40% 40%, var(--teal) 0%, var(--teal-dark) 55%, var(--deep) 100%),
      linear-gradient(90deg, var(--teal-dark) 0%, var(--deep) 100%);
  }

  .slider__title {
    position: absolute;
    left: 243px;
    top: 218px;
    width: 930px;
    font-family: "Anton", "Impact", sans-serif;
    font-size: 84px;
    line-height: 1;
    letter-spacing: -1px;
    text-transform: uppercase;
    white-space: nowrap;
    color: var(--title-mid);
    background: linear-gradient(180deg, var(--title-light) 0%, var(--title-mid) 55%, var(--teal-dark) 100%);
    -webkit-background-clip: text;
    background-clip: text;
    -webkit-text-fill-color: transparent;
    filter:
      drop-shadow(1px 1px 0 var(--title-shadow))
      drop-shadow(2px 2px 0 var(--title-shadow))
      drop-shadow(3px 3px 0 var(--title-shadow))
      drop-shadow(4px 5px 4px rgba(0, 0, 0, 0.7));
  }

  .slider__bullets {
    position: absolute;
    left: 56px;
    top: 420px;
    list-style: none;
    font-family: "Michroma", "Verdana", sans-serif;
    font-size: 14px;
    letter-spacing: 2px;
    text-transform: uppercase;
    color: var(--bullet-text);
  }

  .slider__bullet {
    position: relative;
    padding-left: 47px;
    height: 29px;
    line-height: 29px;
  }

  .slider__bullet::before {
    content: "-";
    position: absolute;
    left: 0;
  }
</style>
</head>
<body>
  <main class="canvas">
    <section class="slider">
      <div class="slider__photo" role="img" aria-label="Photograph of a hand holding a flashlight, its teal-white beam lighting a textured wall from the right"></div>
      <h1 class="slider__title">The Marbled QZ Database</h1>
      <ul class="slider__bullets">
        <li class="slider__bullet">Guide to understanding the QZ database</li>
        <li class="slider__bullet">Data sources, uses and relationships explained with illustrations</li>
        <li class="slider__bullet">New content! Customers</li>
      </ul>
    </section>
  </main>
</body>
</html>
```